Business Card Design Project

Business Card
We are rebranding with a new logo
Industry/Entity Type
Business
Contact Information for Business Card
Doug Farrow +61 457820913 doug@lumora.com.au P.O. Box 728 Kelmscott QLD 4309
Requirements
Must have
- Logo

```html
<!DOCTYPE html>
<html lang="en">
<head>
<meta charset="utf-8">
<title>Lumora International – Business Card</title>
<link rel="stylesheet" href="https://fonts.googleapis.com/css2?family=Exo+2:wght@400;500;600&display=swap">
<style>
  :root {
    --backdrop: #e9e9e7;
    --card: #f7f7f5;
    --gold: #c8961e;
    --brand-blue: #1f7fb8;
    --shadow: rgba(0, 0, 0, 0.12);
  }
  html, body {
    margin: 0;
    padding: 0;
    width: 1200px;
    height: 836px;
    overflow: hidden;
    background: var(--backdrop);
  }
  .canvas {
    position: relative;
    width: 1200px;
    height: 836px;
  }
  .card {
    position: absolute;
    left: 40px;
    top: 100px;
    width: 1120px;
    height: 637px;
    background: var(--card);
    box-shadow: 0 2px 10px var(--shadow);
    font-family: "Exo 2", sans-serif;
  }
  .brand {
    position: absolute;
    left: 108px;
    top: 452px;
    display: flex;
    align-items: center;
    gap: 14px;
  }
  .brand-dot {
    width: 34px;
    height: 34px;
    border-radius: 50%;
    background: var(--brand-blue);
  }
  .brand-name {
    font-size: 30px;
    font-weight: 600;
    color: var(--brand-blue);
    letter-spacing: 0.5px;
    white-space: nowrap;
  }
  .holder-name {
    position: absolute;
    left: 463px;
    bottom: 88px;
    writing-mode: vertical-rl;
    transform: rotate(180deg);
    font-size: 25px;
    font-weight: 500;
    line-height: 37px;
    letter-spacing: 1.5px;
    color: var(--gold);
    text-transform: uppercase;
  }
  .contact {
    position: absolute;
    left: 569px;
    top: 418px;
    font-size: 22px;
    font-weight: 500;
    line-height: 35px;
    letter-spacing: 0.8px;
    color: var(--gold);
  }
  .contact p { margin: 0; }
  .contact .postal { margin-top: 37px; }
</style>
</head>
<body>
  <div class="canvas">
    <section class="card">
      <div class="brand">
        <span class="brand-dot"></span>
        <span class="brand-name">Lumora International</span>
      </div>
      <div class="holder-name">Doug<br>Farrow</div>
      <div class="contact">
        <p>Cell: +61 457820913</p>
        <p>Mob: doug@lumora.com.au</p>
        <p class="postal">P.O. Box 728 Kelmscott QLD 4309</p>
      </div>
    </section>
  </div>
</body>
</html>
```